Harbinger Cargo needs a business card design.

Design a double-sided business card for new freight business. On the front, would like to see our logo along with the following info:

Malcolm Strathby
CEO/FOUNDER
555-207-4163
malcolmstrathby@harbinger-cargo.example

On the reverse side, we would like to use the graphic image of our logo only without the Harbinger Cargo name.

```html
<!DOCTYPE html>
<html lang="en">
<head>
<meta charset="utf-8">
<title>Harbinger Cargo — Business Card</title>
<link href="https://fonts.googleapis.com/css2?family=Lato:wght@400;700;900&display=swap" rel="stylesheet">
<style>
  :root {
    --navy: #1f1a52;
    --navy-light: #2e2870;
    --red: #b11e27;
    --ink: #1b1b1b;
    --paper: #ffffff;
    --backdrop: #e9e9ec;
  }
  * { box-sizing: border-box; margin: 0; padding: 0; }
  html, body {
    width: 1200px; height: 1108px; overflow: hidden;
    background: var(--backdrop);
    font-family: "Lato", Arial, sans-serif;
  }
  .stage {
    position: relative; width: 1200px; height: 1108px;
    display: flex; justify-content: center; align-items: center; gap: 80px;
  }
  .card {
    position: relative; width: 400px; height: 680px;
    border-radius: 22px; overflow: hidden;
    box-shadow: 0 10px 30px rgba(0,0,0,.18);
  }
  .card-front {
    background: var(--paper);
    display: flex; flex-direction: column; align-items: center;
  }
  .brand {
    margin-top: 150px;
    display: flex; align-items: center; gap: 14px;
  }
  .brand-square { width: 22px; height: 22px; background: var(--navy); }
  .brand-name {
    font-weight: 900; font-size: 34px; color: var(--navy);
    letter-spacing: .5px;
  }
  .person { margin-top: 170px; text-align: center; }
  .person-name { font-weight: 700; font-size: 30px; color: var(--navy); }
  .person-name .surname { color: var(--red); }
  .person-title { font-size: 18px; letter-spacing: 1px; color: var(--ink); margin-top: 2px; }
  .divider { width: 70px; height: 1.5px; background: var(--ink); margin: 10px auto 0; }
  .contact-icons { display: flex; gap: 18px; justify-content: center; margin-top: 34px; }
  .contact-icons svg { width: 18px; height: 18px; }
  .contact { text-align: center; margin-top: 8px; font-size: 17px; color: var(--ink); line-height: 1.35; }
  .contact .email { font-size: 15px; }
  .card-back { background: var(--navy); }
  .back-pattern {
    position: absolute; left: 0; top: 0; width: 100%; height: 480px;
    background: linear-gradient(160deg, var(--navy-light) 0%, var(--navy) 85%);
  }
  .back-mark {
    position: absolute; left: 44px; bottom: 88px;
    width: 60px; height: 60px; background: var(--paper);
  }
</style>
</head>
<body>
<main class="stage">
  <section class="card card-front" aria-label="Card front">
    <div class="brand">
      <span class="brand-square"></span>
      <span class="brand-name">Harbinger Cargo</span>
    </div>
    <div class="person">
      <h1 class="person-name">Malcolm <span class="surname">Strathby</span></h1>
      <p class="person-title">CEO/FOUNDER</p>
      <div class="divider"></div>
    </div>
    <div class="contact-icons">
      <svg viewBox="0 0 24 24" fill="none" stroke="#b11e27" stroke-width="2" stroke-linecap="round" stroke-linejoin="round" aria-label="Phone"><path d="M22 16.9v3a2 2 0 0 1-2.2 2 19.8 19.8 0 0 1-8.6-3.1 19.5 19.5 0 0 1-6-6A19.8 19.8 0 0 1 2.1 4.2 2 2 0 0 1 4.1 2h3a2 2 0 0 1 2 1.7c.1.9.4 1.8.7 2.7a2 2 0 0 1-.5 2.1L8 9.8a16 16 0 0 0 6 6l1.3-1.3a2 2 0 0 1 2.1-.4c.9.3 1.8.6 2.7.7a2 2 0 0 1 1.7 2z"/></svg>
      <svg viewBox="0 0 24 24" fill="none" stroke="#b11e27" stroke-width="2" stroke-linejoin="round" aria-label="Email"><rect x="2" y="5" width="20" height="14" rx="1"/><path d="M2 6l10 7 10-7"/></svg>
    </div>
    <div class="contact">
      <p class="phone">555-207-4163</p>
      <p class="email">malcolmstrathby@harbinger-cargo.example</p>
    </div>
  </section>

  <section class="card card-back" aria-label="Card back">
    <div class="back-pattern" role="img" aria-label="Faint repeating brand mark pattern"></div>
    <div class="back-mark" role="img" aria-label="Brand mark"></div>
  </section>
</main>
</body>
</html>
```